Feral Tundra, a 3d voxel survival video game needs a card for gaming conventions

I am the lead developer for Feral Tundra http://www.FeralTundra.example and need a business card to hand out at an indie gaming convention
The card would need to include the game name, website url, my name, position (Lead Developer), e-mail and phone number
The game is a 3d, voxel (with smooth terrain) based survival game with guns and wildlife. The main icon of the game would likely be a grizzly bear but I am willing to accept other designs too.
Attached is a media kit for the game with some images you can use but don't have to its just what little art I can provide. Anything on the website or from the video game can also be used. unrelated art can also be used.
Target Market(s)
Indie Developers/publishers at conferences
Industry/Entity Type
Games
Contact Information for Business Card
Name: Corin Wexford
Position: Lead Developer
E-mail: Gray_Lanterns@mailnest.example
Phone number: 555-372-9186
Look and feel

```html
<!DOCTYPE html>
<html lang="en">
<head>
<meta charset="utf-8">
<title>Feral Tundra – Business Card</title>
<link href="https://fonts.googleapis.com/css2?family=Archivo:wght@400;800&display=swap" rel="stylesheet">
<style>
  :root{
    --page:#d9d4cc;
    --card-black:#0b0b0c;
    --stone-dark:#2b2c2d;
    --stone-mid:#4a4b4a;
    --stone-green:#3c4a37;
    --logo-red:#c23a2a;
    --name-red:#c8201d;
    --text-white:#f2f2f2;
  }
  *{box-sizing:border-box;margin:0;padding:0}
  html,body{width:1200px;height:892px;overflow:hidden}
  body{background:var(--page);font-family:"Archivo",Arial,sans-serif;position:relative}

  .card{position:absolute;left:260px;width:680px;height:388px;overflow:hidden;
        box-shadow:0 6px 18px rgba(0,0,0,.25)}
  .card--front{top:36px}
  .card--back{top:468px;background:var(--card-black);display:flex;align-items:center;justify-content:center}

  .front-art{position:absolute;inset:0;
    background:
      radial-gradient(ellipse at 62% 55%, var(--stone-mid) 0%, transparent 55%),
      linear-gradient(180deg, var(--stone-dark) 0%, #353736 60%, var(--stone-green) 100%)}

  .wordmark{font-weight:800;color:var(--logo-red);text-transform:uppercase;line-height:.95;letter-spacing:.06em}
  .wordmark span{display:block}
  .wordmark span + span{padding-left:1.1em}

  .card--front .wordmark{position:absolute;left:92px;top:28px;font-size:58px}
  .card--back .wordmark{font-size:74px;text-align:left}

  .holder{position:absolute;left:30px;top:190px}
  .holder-name{font-weight:800;font-size:22px;color:var(--name-red);letter-spacing:.04em}
  .holder-role{font-weight:800;font-size:13px;color:var(--text-white);letter-spacing:.06em;margin-top:2px}

  .contacts{position:absolute;left:30px;top:252px;list-style:none}
  .contacts li{display:flex;align-items:center;gap:12px;height:30px;
               font-size:18px;color:var(--text-white);letter-spacing:.08em}
  .contacts svg{width:14px;height:14px;flex:none}
</style>
</head>
<body>

<section class="card card--front">
  <div class="front-art" role="img" aria-label="Dim in-game scene: a player character in a leather jacket standing before a mossy rock wall with trees at dusk"></div>

  <h1 class="wordmark"><span>Feral</span><span>Tundra</span></h1>

  <div class="holder">
    <p class="holder-name">Corin Wexford</p>
    <p class="holder-role">Lead Developer</p>
  </div>

  <ul class="contacts">
    <li>
      <svg viewBox="0 0 14 14" aria-hidden="true"><path d="M3 1h3l1 3-2 1c.7 1.7 1.9 3 3.6 3.7l1-2 3.4 1v3c0 1-1 2-2 2C6 13 1 8 1 3c0-1 1-2 2-2z" fill="#f2f2f2"/></svg>
      555-372-9186
    </li>
    <li>
      <svg viewBox="0 0 14 14" aria-hidden="true"><rect x="1" y="3" width="12" height="8" fill="#f2f2f2"/><path d="M1 3l6 5 6-5" fill="none" stroke="#2b2c2d" stroke-width="1.2"/></svg>
      Gray_Lanterns@mailnest.example
    </li>
    <li>
      <svg viewBox="0 0 14 14" aria-hidden="true"><circle cx="7" cy="7" r="6" fill="#f2f2f2"/><path d="M1 7h12M7 1c-3 3-3 9 0 12M7 1c3 3 3 9 0 12" fill="none" stroke="#2b2c2d" stroke-width="1"/></svg>
      www.FeralTundra.example
    </li>
  </ul>
</section>

<section class="card card--back">
  <h2 class="wordmark"><span>Feral</span><span>Tundra</span></h2>
</section>

</body>
</html>
```